Upscale business cards needed for Board of Directors

We need professional business cards created for members of our family business Board of Directors. We would like these relatively simple and straightforward, but also with a unique element to set them apart. Probably stick with neutral and simple colors - white, grey etc. We need space for the traditional elements, including name, title, address, email/phone number. And we will be creating several from this template so it needs to be template that is easy to switch information in and out of.
Business
See description

```html
<!DOCTYPE html>
<html lang="en">
<head>
<meta charset="utf-8">
<title>Harbourline Holdings – Business Card</title>
<link rel="stylesheet" href="https://fonts.googleapis.com/css2?family=Saira+Condensed:wght@400;500;700&display=swap">
<style>
  :root {
    --page-bg: #e4e4e4;
    --ink: #232323;
    --gold: #bca679;
    --silver-light: #ffffff;
    --silver-mid: #d9d9d9;
    --icon: #f4f4f4;
  }
  * { margin: 0; padding: 0; box-sizing: border-box; }
  html, body {
    width: 1200px; height: 841px; overflow: hidden;
    background: var(--page-bg);
    font-family: "Saira Condensed", "Arial Narrow", sans-serif;
  }
  .card {
    position: absolute; left: 80px; top: 121px;
    width: 1040px; height: 598px;
    overflow: hidden;
    background: linear-gradient(90deg, var(--silver-mid) 0%, var(--silver-light) 30%, var(--silver-light) 70%, var(--silver-mid) 100%);
  }
  .card-shapes { position: absolute; inset: 0; }
  .accent-bar {
    position: absolute; left: 253px; top: 46px; width: 490px; height: 10px;
    background: var(--gold);
  }
  .company-name {
    position: absolute; left: 0; width: 1040px; top: 84px;
    text-align: center; color: var(--ink);
    font-size: 72px; font-weight: 700; line-height: 1.1;
  }
  .person {
    position: absolute; right: 634px; top: 342px; text-align: right; color: var(--ink);
  }
  .person-name { font-size: 33px; font-weight: 700; letter-spacing: 1px; line-height: 1.2; }
  .person-title { font-size: 32px; font-weight: 400; line-height: 1.3; }
  .divider {
    position: absolute; left: 435px; top: 305px; width: 5px; height: 192px;
    background: linear-gradient(180deg, #ffffff, #cfcfcf);
  }
  .contact-list { position: absolute; left: 462px; top: 318px; list-style: none; }
  .contact-item {
    display: flex; align-items: center; height: 66px;
    font-size: 31px; color: var(--ink);
  }
  .contact-item svg { width: 40px; height: 40px; margin-right: 18px; flex: none; }
  .website {
    position: absolute; left: 0; width: 1040px; top: 548px; text-align: center;
    font-size: 28px; font-weight: 700; letter-spacing: 3px; color: var(--ink); line-height: 1.3;
  }
</style>
</head>
<body>
  <div class="card">
    <svg class="card-shapes" viewBox="0 0 1040 598" width="1040" height="598">
      <defs>
        <linearGradient id="silverBand" x1="0" x2="1" y1="0" y2="0">
          <stop offset="0" stop-color="#9a9a9a"/>
          <stop offset="0.45" stop-color="#f2f2f2"/>
          <stop offset="0.75" stop-color="#ffffff"/>
          <stop offset="1" stop-color="#8e8e8e"/>
        </linearGradient>
      </defs>
      <path d="M0 290 Q 560 215 1040 262 L1040 540 L0 540 Z" fill="url(#silverBand)"/>
      <path d="M0 302 Q 560 238 1040 282 L1040 540 L0 540 Z" fill="var(--gold)"/>
      <path d="M0 290 Q 560 215 1040 262" fill="none" stroke="var(--ink)" stroke-width="5"/>
    </svg>

    <div class="accent-bar"></div>
    <div class="company-name">HARBOURLINE HOLDINGS</div>

    <div class="person">
      <div class="person-name">YOUR NAME</div>
      <div class="person-title">Position</div>
    </div>

    <div class="divider"></div>

    <ul class="contact-list">
      <li class="contact-item">
        <svg viewBox="0 0 40 40" aria-hidden="true"><rect x="10" y="2" width="20" height="36" rx="3" fill="none" stroke="var(--icon)" stroke-width="3"/><rect x="14" y="7" width="12" height="22" fill="var(--icon)" opacity="0.6"/></svg>
        <span>012 345 67890</span>
      </li>
      <li class="contact-item">
        <svg viewBox="0 0 40 40" aria-hidden="true"><path d="M3 14 L20 4 L37 14 L37 34 L3 34 Z" fill="var(--icon)"/><path d="M3 14 L20 25 L37 14" fill="none" stroke="#b9b9b9" stroke-width="2"/></svg>
        <span>yourname@harbourlineholdings.com</span>
      </li>
      <li class="contact-item">
        <svg viewBox="0 0 40 40" aria-hidden="true"><path d="M2 20 L20 5 L38 20 Z" fill="var(--icon)"/><rect x="8" y="20" width="24" height="16" fill="var(--icon)"/><rect x="17" y="25" width="7" height="11" fill="var(--gold)"/></svg>
        <span>Address</span>
      </li>
    </ul>

    <div class="website">www.harbourlineholdings.com</div>
  </div>
</body>
</html>
```